need a Flyer for Plush Toy company

Need a Flyer for Plush Toy company ,

I upload a file for TEXT

Target Market(s)

Toys wholesalers , Supermarket

Industry/Entity Type

Toy Store

Colors
000000
ec1f27
c4c4c4

Requirements
Must have
• I have up loaded 3 files
• 1. Logo Registered Brand
• 2. customer's design in drawing
• 3. our ready samples based on Design
Nice to have
• happy kids in Nature ,
• happy kids in Ski ,
• different color Kids ,
• Multi culture concept

```html
<!DOCTYPE html>
<html lang="en">
<head>
<meta charset="utf-8">
<title>Nubo Tami – Plush Toys Flyer</title>
<link rel="stylesheet" href="https://fonts.googleapis.com/css2?family=Fredoka:wght@600;700&family=Lilita+One&family=Kalam:wght@400&family=Patrick+Hand&family=Open+Sans:ital,wght@0,400;1,400&display=swap">
<style>
  :root {
    --red: #ec1f27;
    --red-deep: #c3121a;
    --black: #000000;
    --ink: #1e1e1e;
    --grey: #c4c4c4;
    --white: #ffffff;
    --yellow: #fff200;
    --sky: #5cb7d6;
  }
  * { margin: 0; padding: 0; box-sizing: border-box; }
  html, body { width: 889px; height: 1200px; overflow: hidden; background: var(--white); }
  .flyer { position: relative; width: 889px; height: 1200px; overflow: hidden; background: var(--white); font-family: "Open Sans", sans-serif; }

  .hero-photo {
    position: absolute; left: 212px; top: 0; width: 677px; height: 560px;
    background: linear-gradient(90deg, rgba(255,255,255,1) 0%, rgba(255,255,255,0) 28%),
                linear-gradient(160deg, #6fc3df 0%, var(--sky) 45%, #3f9dc0 100%);
  }
  .background-shapes { position: absolute; inset: 0; }

  .brand { position: absolute; left: 70px; top: 95px; display: flex; align-items: center; gap: 10px; }
  .brand-dot { width: 22px; height: 22px; border-radius: 50%; background: var(--red); }
  .brand-name { font-family: "Fredoka", sans-serif; font-weight: 700; font-size: 34px; color: var(--ink); }
  .tagline { position: absolute; left: 64px; top: 192px; font-family: "Kalam", cursive; font-size: 27px; color: var(--red-deep); }

  .title { position: absolute; font-family: "Fredoka", sans-serif; font-weight: 700; color: var(--red); line-height: 1; }
  .title-first { left: 52px; top: 262px; font-size: 132px; }
  .title-second { left: 200px; top: 358px; font-size: 132px; }

  .family-badge {
    position: absolute; left: 244px; top: 490px; width: 306px; height: 66px;
    background: var(--black); transform: rotate(-4deg);
    display: flex; align-items: center; justify-content: center;
    font-family: "Patrick Hand", sans-serif; font-size: 40px; color: var(--white);
  }

  .subtitle { position: absolute; left: 41px; top: 578px; font-family: "Patrick Hand", sans-serif; font-size: 31px; color: var(--white); }
  .trader-badge {
    position: absolute; left: 46px; top: 630px; width: 478px; height: 60px;
    background: var(--black); transform: rotate(-2deg);
    display: flex; align-items: center; justify-content: center; gap: 10px;
    font-family: "Lilita One", sans-serif; font-size: 34px;
  }
  .trader-badge .accent { color: var(--yellow); }
  .trader-badge .plain { color: var(--white); }

  .about { position: absolute; left: 41px; top: 703px; width: 520px; color: var(--white); font-style: italic; font-size: 14.4px; line-height: 21px; }
  .about p { margin-bottom: 8px; }

  .sample-art { position: absolute; left: 51px; top: 920px; width: 456px; height: 156px; border-radius: 10px;
    background: linear-gradient(180deg, #f6e8b8 0%, #c9e5b7 45%, #9fd1a7 100%); }

  .photo-frame { position: absolute; background: var(--white); padding: 10px; box-shadow: 0 6px 14px rgba(0,0,0,.35); }
  .photo-frame .photo { width: 100%; height: 100%; }
  .frame-one { left: 584px; top: 568px; width: 270px; height: 134px; transform: rotate(-3deg); }
  .frame-two { left: 618px; top: 712px; width: 250px; height: 152px; transform: rotate(2deg); }
  .frame-three { left: 600px; top: 894px; width: 256px; height: 158px; transform: rotate(-2deg); }
  .photo-baby { background: linear-gradient(160deg, #f4efe8, #d9c9b3); }
  .photo-ski { background: linear-gradient(180deg, #7fb4e6 0%, #c8ddf0 45%, #f2f5f8 100%); }
  .photo-bed { background: linear-gradient(160deg, #eef0f2, #c9b7a0); }

  .footer { position: absolute; left: 0; top: 1080px; width: 889px; height: 120px; background: linear-gradient(180deg, #2b2b2b, var(--ink)); }
  .contact { position: absolute; display: flex; align-items: center; gap: 10px; color: var(--white); font-size: 13px; }
  .contact svg { width: 16px; height: 16px; flex: none; }
  .vat-label { color: var(--yellow); }
  .bank { position: absolute; left: 644px; top: 1132px; font-size: 11px; font-style: italic; color: var(--white); line-height: 16px; }
  .bank .label { color: var(--red); }
</style>
</head>
<body>
<main class="flyer">
  <div class="hero-photo" role="img" aria-label="Photo of a laughing toddler in a striped shirt lying on a blue blanket among plush toys"></div>

  <svg class="background-shapes" width="889" height="1200" viewBox="0 0 889 1200" aria-hidden="true">
    <path d="M0,455 C70,425 125,450 150,485 C185,530 240,548 320,542 L600,532 C720,526 820,505 889,485 L889,520 C820,540 720,560 600,566 L320,575 C240,580 180,560 140,520 C115,490 60,478 0,490 Z" fill="#2a2a2a"/>
    <path d="M0,478 C65,462 120,478 145,508 C182,552 240,572 320,568 L600,558 C720,552 820,532 889,512 L889,1090 C740,1040 560,1105 330,1080 C170,1064 70,1085 0,1068 Z" fill="var(--red)"/>
    <path d="M0,1060 C90,1080 180,1060 330,1072 C560,1096 740,1030 889,1078 L889,1092 C740,1046 560,1110 330,1086 C180,1072 90,1092 0,1074 Z" fill="var(--white)"/>
  </svg>

  <div class="brand"><span class="brand-dot"></span><span class="brand-name">Nubo Tami</span></div>
  <p class="tagline">Have you been there?</p>

  <h1 class="title title-first">Nubo</h1>
  <h1 class="title title-second">Tami</h1>
  <div class="family-badge">Family Business</div>

  <p class="subtitle">Innovative Developer for Plush Toys</p>
  <div class="trader-badge"><span class="accent">International Trader</span><span class="plain">for Toys</span></div>

  <div class="about">
    <p>We live and work in Lindenfeld near to Cologne Germany. We speak German and English.</p>
    <p>The toys are made in China, we are small family business , but we are professional in Plush toys business , right now we have successfully launched Projects with a huge Japanese 100 Yen Chain Store. Here in Flyer we show a Sample project.</p>
    <p>100 Yen = 0.90 USD , Our products can meet strictest Quality Control , but are with extremely Low Price to fit for Japanese Dollar Shop as well as his overseas Store around the world.</p>
  </div>

  <div class="sample-art" role="img" aria-label="Sample plush characters in pastel colours sitting on a mint green sofa"></div>

  <figure class="photo-frame frame-one"><div class="photo photo-baby" role="img" aria-label="Photo of a smiling baby in a knitted hat with soft toys"></div></figure>
  <figure class="photo-frame frame-two"><div class="photo photo-ski" role="img" aria-label="Photo of two children in colourful ski suits on a snowy mountain"></div></figure>
  <figure class="photo-frame frame-three"><div class="photo photo-bed" role="img" aria-label="Photo of a baby on a bed surrounded by plush animals"></div></figure>

  <footer class="footer"></footer>

  <div class="contact" style="left:35px;top:1119px">
    <svg viewBox="0 0 16 16"><circle cx="8" cy="8" r="8" fill="var(--red)"/><path d="M5 4.5l1.6-.4 1 2-1 .8a5 5 0 0 0 2.5 2.5l.8-1 2 1-.4 1.6c-3.6.3-6.8-2.9-6.5-6.5z" fill="#fff"/></svg>
    <span>+49 (0) 2201- 400 1234</span>
  </div>
  <div class="contact" style="left:35px;top:1143px">
    <svg viewBox="0 0 16 16"><circle cx="8" cy="8" r="8" fill="var(--red)"/><rect x="4" y="5" width="8" height="6" fill="#fff"/><path d="M4 5l4 3 4-3" fill="none" stroke="var(--red)" stroke-width="1"/></svg>
    <span>hello@nubotami.de</span>
  </div>
  <div class="contact" style="left:35px;top:1167px">
    <svg viewBox="0 0 16 16"><circle cx="8" cy="8" r="8" fill="var(--red)"/><path d="M8 3.5a3 3 0 0 0-3 3c0 2.3 3 6 3 6s3-3.7 3-6a3 3 0 0 0-3-3z" fill="#fff"/><circle cx="8" cy="6.5" r="1.1" fill="var(--red)"/></svg>
    <span>Lindenweg 7, 50999 Lindenfeld Germany</span>
  </div>

  <div class="contact" style="left:371px;top:1119px">
    <svg viewBox="0 0 16 16"><circle cx="8" cy="8" r="8" fill="var(--red)"/><rect x="4" y="6" width="8" height="5" fill="#fff"/><rect x="5.5" y="4" width="5" height="2.5" fill="#fff"/></svg>
    <span>+49 (0) 2201- 400 1240</span>
  </div>
  <div class="contact" style="left:371px;top:1143px">
    <svg viewBox="0 0 16 16"><rect x="4.5" y="1.5" width="7" height="13" rx="1.5" fill="none" stroke="var(--red)" stroke-width="1.3"/><circle cx="8" cy="12" r=".8" fill="var(--red)"/></svg>
    <span>+49 (0) 170 5550 123</span>
  </div>
  <div class="contact" style="left:397px;top:1167px">
    <span><span class="vat-label">Ust-IdNr./VAT No.</span> DE123456789</span>
  </div>

  <div class="bank">
    <div><span class="label">Kontainhaber/Account Holder:</span>&nbsp; Mia Lorenz</div>
    <div><span class="label">IBAN:</span>&nbsp; DE00 1234 5678 9012 3456 00</div>
    <div><span class="label">BIC :</span>&nbsp; ABCDDEFF000</div>
  </div>
</main>
</body>
</html>
```